Forest Consultant/Timber Buyer needs a clean business card

We are a forestry consulting and timber buying company. We meet with private landowners and assist them with timber management and timber harvesting. We would like a professional business card, please no clip art. logo is blue and white but would like to see a gray,silver, or some other color incorporated. Would like basic contact info. Would like to the layout to be creative and sleek but masculine.

Target Market(s)

private landowners

Industry/Entity Type

Business

Contact Information for Business Card

name,position, cell number, office number, email, website. This might be to cluttered. Basic contact info is what we are looking for.

Contact info can all be on one side with logo on the other.

Font styles to use
Serif
Sans Serif

Colors
0255a3
ffffff
aaaaaa

Requirements
Must have
• We just want it professional.
Nice to have
• Creative layout.
Should not have
• please no clip art of log trucks etc.

```html
<!DOCTYPE html>
<html lang="en">
<head>
<meta charset="utf-8">
<title>Northgate Forest &amp; Land – Business Card</title>
<link href="https://fonts.googleapis.com/css2?family=Open+Sans:wght@400;600;700&display=swap" rel="stylesheet">
<style>
  :root {
    --brand-blue: #0255a3;
    --brand-white: #ffffff;
    --brand-silver: #aaaaaa;
    --ink-dark: #333333;
    --stage: #2e2e2e;
  }
  * { margin: 0; padding: 0; box-sizing: border-box; }
  html, body { width: 1200px; height: 900px; overflow: hidden; }
  body {
    background: var(--stage);
    font-family: "Open Sans", Arial, sans-serif;
    position: relative;
  }
  .card {
    position: absolute;
    width: 520px;
    height: 300px;
    border-radius: 22px;
    overflow: hidden;
  }
  /* Back side */
  .card-back {
    left: 60px;
    top: 140px;
    background: var(--brand-silver);
    display: flex;
    align-items: center;
    justify-content: center;
    gap: 14px;
  }
  .back-mark {
    width: 26px; height: 26px;
    border-radius: 50%;
    background: var(--brand-blue);
  }
  .back-name {
    color: var(--brand-blue);
    font-weight: 700;
    font-size: 30px;
    letter-spacing: 1px;
  }
  /* Front side */
  .card-front {
    left: 620px;
    top: 460px;
    background: var(--brand-white);
  }
  .front-bands { position: absolute; inset: 0; }
  .front-logo {
    position: absolute;
    left: 40px;
    top: 58px;
    display: flex;
    align-items: center;
    gap: 10px;
  }
  .front-logo .logo-dot {
    width: 18px; height: 18px;
    border-radius: 50%;
    background: var(--brand-blue);
  }
  .front-logo .logo-name {
    color: var(--brand-blue);
    font-weight: 700;
    font-size: 24px;
    letter-spacing: 0.5px;
  }
  .person {
    position: absolute;
    left: 40px;
    top: 226px;
    color: var(--brand-white);
  }
  .person-name { font-weight: 700; font-size: 21px; letter-spacing: 0.5px; }
  .person-role { font-size: 12px; letter-spacing: 1px; text-align: right; }
  .divider {
    position: absolute;
    left: 238px;
    top: 180px;
    width: 1px;
    height: 92px;
    background: var(--brand-white);
    opacity: 0.8;
  }
  .contacts {
    position: absolute;
    left: 256px;
    top: 178px;
    list-style: none;
    color: var(--brand-white);
    font-size: 13px;
    line-height: 23px;
  }
  .contacts li { display: flex; align-items: center; gap: 8px; }
  .contacts svg { width: 11px; height: 11px; flex: none; }
</style>
</head>
<body>

<section class="card card-back" aria-label="Card back">
  <span class="back-mark"></span>
  <span class="back-name">NORTHGATE FOREST &amp; LAND</span>
</section>

<section class="card card-front" aria-label="Card front">
  <svg class="front-bands" viewBox="0 0 520 300" preserveAspectRatio="none" aria-hidden="true">
    <path d="M0,176 Q250,226 520,92 L520,104 Q250,238 0,188 Z" fill="var(--brand-silver)"/>
    <path d="M0,190 Q250,240 520,106 L520,300 L0,300 Z" fill="var(--brand-blue)"/>
  </svg>

  <div class="front-logo">
    <span class="logo-dot"></span>
    <span class="logo-name">NORTHGATE FOREST &amp; LAND</span>
  </div>

  <div class="person">
    <div class="person-name">MARK ELLISON</div>
    <div class="person-role">DIRECTOR</div>
  </div>

  <div class="divider"></div>

  <ul class="contacts">
    <li><svg viewBox="0 0 12 12"><path d="M2 1h3l1 3-1.5 1a6 6 0 0 0 2.5 2.5L8 6l3 1v3a1 1 0 0 1-1 1A9 9 0 0 1 1 2a1 1 0 0 1 1-1z" fill="currentColor"/></svg>+330 4815-2260</li>
    <li><svg viewBox="0 0 12 12"><rect x="3" y="0.5" width="6" height="11" rx="1" fill="none" stroke="currentColor"/><circle cx="6" cy="9.5" r="0.7" fill="currentColor"/></svg>+330 3927-5184</li>
    <li><svg viewBox="0 0 12 12"><rect x="0.5" y="2" width="11" height="8" fill="none" stroke="currentColor"/><path d="M0.5 2 6 6.5 11.5 2" fill="none" stroke="currentColor"/></svg>info@northgateforest.com</li>
    <li><svg viewBox="0 0 12 12"><circle cx="6" cy="6" r="5.3" fill="none" stroke="currentColor"/><ellipse cx="6" cy="6" rx="2.2" ry="5.3" fill="none" stroke="currentColor"/><path d="M0.7 6h10.6" stroke="currentColor"/></svg>www.northgateforest.com</li>
  </ul>
</section>

</body>
</html>
```